quiet orchard

It is a small business that is looking to sell medical supplies and services. later down the line it will branch off to help solve other world problems, i.e. global warming and raw material shortages.
but we will start with hospital equipment and supplies.

Target Market(s)

all medical facilities

Coding

Coded - Design and coding required

Number of Pages Required

1 page

```html
<!DOCTYPE html>
<html lang="en">
<head>
<meta charset="utf-8">
<title>Quiet Orchard</title>
<link href="https://fonts.googleapis.com/css2?family=Roboto:wght@400;500;700&display=swap" rel="stylesheet">
<style>
:root{
  --primary:#7e1437;
  --primary-dark:#5f0d2a;
  --footer:#6a0f2f;
  --text:#222;
  --muted:#6b6b6b;
  --star:#e3c21a;
  --white:#fff;
}
*{box-sizing:border-box;margin:0;padding:0}
html,body{width:1200px;height:3074px;overflow:hidden}
body{position:relative;font-family:'Roboto',sans-serif;color:var(--text);background:var(--white)}
a{color:inherit;text-decoration:none}
.abs{position:absolute}

.topbar{left:0;top:0;width:1200px;height:45px;background:var(--primary);color:var(--white);font-size:13px;font-weight:500}
.topbar .item{position:absolute;top:14px;display:flex;align-items:center;gap:10px}
.topbar svg{width:14px;height:14px;fill:var(--white)}

.header{left:0;top:45px;width:1200px;height:141px}
.logo{position:absolute;left:124px;top:42px;display:flex;align-items:center;gap:8px;color:var(--primary);font-weight:700;font-size:22px;line-height:24px;text-align:center}
.logo .dot{width:12px;height:12px;border-radius:50%;background:var(--primary)}
.nav{position:absolute;left:275px;top:62px;display:flex;gap:41px;font-size:16px;font-weight:500;color:#111}
.btn-contact{position:absolute;left:936px;top:48px;width:152px;height:45px;border-radius:8px;background:var(--primary);color:var(--white);font-size:18px;font-weight:500;display:flex;align-items:center;justify-content:center}

.hero{left:0;top:186px;width:1200px;height:599px;overflow:hidden}
.hero-photo{position:absolute;left:600px;top:0;width:600px;height:599px;background:linear-gradient(160deg,#e9ecef,#c9ced4 55%,#b9a78f)}
.hero-tint{position:absolute;left:0;top:0;width:600px;height:599px;background:linear-gradient(120deg,#a04a6c,#8c2a52 60%,#a3506f)}
.hero h1{position:absolute;left:114px;top:146px;color:var(--white);font-size:60px;line-height:72px;font-weight:700;white-space:nowrap}
.hero p{position:absolute;left:114px;top:303px;width:470px;color:var(--white);font-size:15px;line-height:25px}
.btn-shop{position:absolute;left:115px;top:405px;width:152px;height:45px;border-radius:8px;background:var(--white);color:var(--primary);font-size:19px;font-weight:700;display:flex;align-items:center;justify-content:center}
.dots{position:absolute;left:114px;top:519px;display:flex;gap:5px}
.dots span{width:11px;height:11px;border-radius:50%;background:var(--white)}
.dots span.gap{margin-left:12px}
.hero svg.curve{position:absolute;left:0;top:0;width:1200px;height:599px}

.sec-title{font-size:32px;font-weight:700;text-align:center}
.sec-title .accent{color:var(--primary)}
.sec-title .rest{color:var(--muted)}

.products-title{left:0;top:812px;width:1200px}
.card{position:absolute;top:903px;width:228px;height:296px;background:var(--white);box-shadow:0 0 4px rgba(0,0,0,.18);text-align:center}
.card .thumb{width:110px;height:120px;margin:18px auto 0;border-radius:10px;background:linear-gradient(#eef1f4,#d8dde3)}
.stars{margin-top:18px;display:flex;justify-content:center;gap:2px}
.stars svg{width:17px;height:17px}
.card h3{margin-top:6px;font-size:18px;font-weight:500}
.card .price{margin-top:10px;font-size:14px;font-weight:500}
.card .actions{position:absolute;left:0;bottom:14px;width:100%;display:flex;align-items:center;justify-content:center;gap:30px;color:var(--primary);font-size:17px;font-weight:500}
.card .actions svg{width:22px;height:22px}

.goal{left:0;top:1286px;width:1200px;height:688px;background:linear-gradient(135deg,#8a1d43,#7a1236 45%,#8e2a4d)}
.goal h2{position:absolute;left:0;top:66px;width:1200px;text-align:center;color:var(--white);font-size:40px;font-weight:700}
.goal-card{position:absolute;top:146px;width:461px;height:458px;background:var(--white);padding:5px}
.goal-card .img{width:451px;height:383px}
.goal-card h3{margin-top:26px;text-align:center;font-size:22px;font-weight:500;color:#111}

.about-ring{left:97px;top:2086px;width:442px;height:428px;border-radius:50%;background:var(--primary)}
.about-img{left:112px;top:2084px;width:428px;height:428px;border-radius:50%;background:radial-gradient(circle at 45% 45%,#dfe6f4,#7ea0d8 55%,#b7dba0)}
.about-title{left:599px;top:2055px;font-size:42px;font-weight:700}
.about-title .accent{color:var(--primary)}
.about-title .rest{color:var(--muted)}
.about-text{left:599px;width:492px;color:var(--muted);font-size:13.5px;line-height:24.7px}
.btn-read{left:599px;top:2492px;width:152px;height:45px;border-radius:8px;background:var(--primary);color:var(--white);font-size:19px;font-weight:500;display:flex;align-items:center;justify-content:center}

.footer{left:0;top:2688px;width:1200px;height:330px;background:linear-gradient(100deg,#6e1231,var(--footer))}
.footer svg.curve{position:absolute;left:0;top:0;width:1200px;height:70px}
.footer-logo{position:absolute;left:110px;top:130px;color:var(--white);font-weight:700;font-size:50px;line-height:54px;text-align:center;display:flex;align-items:center;gap:12px}
.footer-logo .dot{width:16px;height:16px;border-radius:50%;background:var(--white)}
.fcol{position:absolute;top:104px;color:var(--white)}
.fcol h4{font-size:22px;font-weight:500;margin-bottom:16px}
.fcol li{list-style:none;font-size:16px;line-height:26.5px}
.fcol p{font-size:17.5px;line-height:26px}
.cart-float{position:absolute;left:1115px;top:2934px;width:64px;height:64px;border-radius:50%;background:var(--white);box-shadow:0 2px 6px rgba(0,0,0,.35);display:flex;align-items:center;justify-content:center}
.cart-float svg{width:36px;height:36px}

.bottombar{left:0;top:3018px;width:1200px;height:56px;background:var(--primary);color:var(--white);font-size:16px}
.bottombar .copy{position:absolute;left:104px;top:18px}
.cards{position:absolute;left:824px;top:14px;display:flex;gap:18px}
.cards span{width:52px;height:28px;border-radius:3px;background:#f1f1f1}
</style>
</head>
<body>

<div class="abs topbar">
  <div class="item" style="left:112px"><svg viewBox="0 0 16 16"><circle cx="8" cy="4.5" r="3.5"/><path d="M1 16c0-5 3-7 7-7s7 2 7 7z"/></svg>Signin or Register</div>
  <div class="item" style="left:294px"><svg viewBox="0 0 16 16"><path d="M8 15 1.5 8.5A4 4 0 0 1 8 3a4 4 0 0 1 6.5 5.5z"/></svg>My Whishlist</div>
  <div class="item" style="left:448px"><svg viewBox="0 0 16 16"><path d="M0 2h3l2 8h9l2-6H5" fill="none" stroke="#fff" stroke-width="1.4"/><circle cx="6" cy="13" r="1.5"/><circle cx="13" cy="13" r="1.5"/></svg>My Cart</div>
  <div class="item" style="left:974px"><svg viewBox="0 0 16 16"><path d="M3 1l3 3-2 2c1 2 3 4 6 6l2-2 3 3-2 2C7 15 1 9 1 3z"/></svg>555 010 4821</div>
</div>

<header class="abs header">
  <div class="logo"><span class="dot"></span><span>QUIET<br>ORCHARD</span></div>
  <nav class="nav">
    <a href="#">HOME</a><a href="#">ABOUT US</a><a href="#">SERVICES</a><a href="#">SHOP</a><a href="#">OUR GOAL</a><a href="#">LATEST NEWS</a>
  </nav>
  <a class="btn-contact" href="#">CONTACT US</a>
</header>

<section class="abs hero">
  <div class="hero-photo" role="img" aria-label="Warehouse shelves stocked with boxed medical supplies"></div>
  <div class="hero-tint" role="img" aria-label="Tinted view of the supply warehouse"></div>
  <svg class="curve" viewBox="0 0 1200 599" preserveAspectRatio="none"><path d="M0 599Q600 463 1200 599Z" fill="#fff"/></svg>
  <h1>WELCOME TO<br>QUIET ORCHARD</h1>
  <p>Contrary to popular belief, Lorem Ipsum is not simply random text. It has roots in a piece of classical Latin literature from 45 BC, making it over 2000 years old. Marcus Ellwood,</p>
  <a class="btn-shop" href="#">SHOP NOW</a>
  <div class="dots"><span></span><span></span><span class="gap"></span></div>
</section>

<h2 class="abs sec-title products-title"><span class="accent">OUR</span> <span class="rest">PRODUCTS</span></h2>

<div class="card" style="left:107px">
  <div class="thumb" role="img" aria-label="Stethoscope"></div>
  <div class="stars"><svg viewBox="0 0 20 20"><path d="M10 1l2.6 6 6.4.5-4.9 4.2 1.5 6.3L10 14.6 4.4 18l1.5-6.3L1 7.5 7.4 7z" fill="#e3c21a"/></svg><svg viewBox="0 0 20 20"><path d="M10 1l2.6 6 6.4.5-4.9 4.2 1.5 6.3L10 14.6 4.4 18l1.5-6.3L1 7.5 7.4 7z" fill="#e3c21a"/></svg><svg viewBox="0 0 20 20"><path d="M10 1l2.6 6 6.4.5-4.9 4.2 1.5 6.3L10 14.6 4.4 18l1.5-6.3L1 7.5 7.4 7z" fill="#e3c21a"/></svg><svg viewBox="0 0 20 20"><path d="M10 1l2.6 6 6.4.5-4.9 4.2 1.5 6.3L10 14.6 4.4 18l1.5-6.3L1 7.5 7.4 7z" fill="#e3c21a"/></svg><svg viewBox="0 0 20 20"><path d="M10 1l2.6 6 6.4.5-4.9 4.2 1.5 6.3L10 14.6 4.4 18l1.5-6.3L1 7.5 7.4 7z" fill="none" stroke="#e3c21a" stroke-width="1.5"/></svg></div>
  <h3>PRODUCT NAME</h3><div class="price">$ 50.00</div>
  <div class="actions"><svg viewBox="0 0 24 24" fill="none" stroke="#444" stroke-width="1.5"><path d="M1 3h4l3 12h12l3-9H6"/><circle cx="9" cy="19" r="1.6"/><circle cx="18" cy="19" r="1.6"/></svg><span>SHOP NOW</span><svg viewBox="0 0 24 24"><path d="M12 21 3 12a5 5 0 0 1 9-7 5 5 0 0 1 9 7z" fill="#111"/></svg></div>
</div>
<div class="card" style="left:360px">
  <div class="thumb" role="img" aria-label="Oxygen mask"></div>
  <div class="stars"><svg viewBox="0 0 20 20"><path d="M10 1l2.6 6 6.4.5-4.9 4.2 1.5 6.3L10 14.6 4.4 18l1.5-6.3L1 7.5 7.4 7z" fill="#e3c21a"/></svg><svg viewBox="0 0 20 20"><path d="M10 1l2.6 6 6.4.5-4.9 4.2 1.5 6.3L10 14.6 4.4 18l1.5-6.3L1 7.5 7.4 7z" fill="#e3c21a"/></svg><svg viewBox="0 0 20 20"><path d="M10 1l2.6 6 6.4.5-4.9 4.2 1.5 6.3L10 14.6 4.4 18l1.5-6.3L1 7.5 7.4 7z" fill="#e3c21a"/></svg><svg viewBox="0 0 20 20"><path d="M10 1l2.6 6 6.4.5-4.9 4.2 1.5 6.3L10 14.6 4.4 18l1.5-6.3L1 7.5 7.4 7z" fill="#e3c21a"/></svg><svg viewBox="0 0 20 20"><path d="M10 1l2.6 6 6.4.5-4.9 4.2 1.5 6.3L10 14.6 4.4 18l1.5-6.3L1 7.5 7.4 7z" fill="none" stroke="#e3c21a" stroke-width="1.5"/></svg></div>
  <h3>PRODUCT NAME</h3><div class="price">$ 50.00</div>
  <div class="actions"><svg viewBox="0 0 24 24" fill="none" stroke="#444" stroke-width="1.5"><path d="M1 3h4l3 12h12l3-9H6"/><circle cx="9" cy="19" r="1.6"/><circle cx="18" cy="19" r="1.6"/></svg><span>SHOP NOW</span><svg viewBox="0 0 24 24"><path d="M12 21 3 12a5 5 0 0 1 9-7 5 5 0 0 1 9 7z" fill="#111"/></svg></div>
</div>
<div class="card" style="left:612px">
  <div class="thumb" role="img" aria-label="Blood glucose meter"></div>
  <div class="stars"><svg viewBox="0 0 20 20"><path d="M10 1l2.6 6 6.4.5-4.9 4.2 1.5 6.3L10 14.6 4.4 18l1.5-6.3L1 7.5 7.4 7z" fill="#e3c21a"/></svg><svg viewBox="0 0 20 20"><path d="M10 1l2.6 6 6.4.5-4.9 4.2 1.5 6.3L10 14.6 4.4 18l1.5-6.3L1 7.5 7.4 7z" fill="#e3c21a"/></svg><svg viewBox="0 0 20 20"><path d="M10 1l2.6 6 6.4.5-4.9 4.2 1.5 6.3L10 14.6 4.4 18l1.5-6.3L1 7.5 7.4 7z" fill="#e3c21a"/></svg><svg viewBox="0 0 20 20"><path d="M10 1l2.6 6 6.4.5-4.9 4.2 1.5 6.3L10 14.6 4.4 18l1.5-6.3L1 7.5 7.4 7z" fill="#e3c21a"/></svg><svg viewBox="0 0 20 20"><path d="M10 1l2.6 6 6.4.5-4.9 4.2 1.5 6.3L10 14.6 4.4 18l1.5-6.3L1 7.5 7.4 7z" fill="none" stroke="#e3c21a" stroke-width="1.5"/></svg></div>
  <h3>PRODUCT NAME</h3><div class="price">$ 50.00</div>
  <div class="actions"><svg viewBox="0 0 24 24" fill="none" stroke="#444" stroke-width="1.5"><path d="M1 3h4l3 12h12l3-9H6"/><circle cx="9" cy="19" r="1.6"/><circle cx="18" cy="19" r="1.6"/></svg><span>SHOP NOW</span><svg viewBox="0 0 24 24"><path d="M12 21 3 12a5 5 0 0 1 9-7 5 5 0 0 1 9 7z" fill="#111"/></svg></div>
</div>
<div class="card" style="left:865px">
  <div class="thumb" role="img" aria-label="Surgical scalpels"></div>
  <div class="stars"><svg viewBox="0 0 20 20"><path d="M10 1l2.6 6 6.4.5-4.9 4.2 1.5 6.3L10 14.6 4.4 18l1.5-6.3L1 7.5 7.4 7z" fill="#e3c21a"/></svg><svg viewBox="0 0 20 20"><path d="M10 1l2.6 6 6.4.5-4.9 4.2 1.5 6.3L10 14.6 4.4 18l1.5-6.3L1 7.5 7.4 7z" fill="#e3c21a"/></svg><svg viewBox="0 0 20 20"><path d="M10 1l2.6 6 6.4.5-4.9 4.2 1.5 6.3L10 14.6 4.4 18l1.5-6.3L1 7.5 7.4 7z" fill="#e3c21a"/></svg><svg viewBox="0 0 20 20"><path d="M10 1l2.6 6 6.4.5-4.9 4.2 1.5 6.3L10 14.6 4.4 18l1.5-6.3L1 7.5 7.4 7z" fill="#e3c21a"/></svg><svg viewBox="0 0 20 20"><path d="M10 1l2.6 6 6.4.5-4.9 4.2 1.5 6.3L10 14.6 4.4 18l1.5-6.3L1 7.5 7.4 7z" fill="none" stroke="#e3c21a" stroke-width="1.5"/></svg></div>
  <h3>PRODUCT NAME</h3><div class="price">$ 50.00</div>
  <div class="actions"><svg viewBox="0 0 24 24" fill="none" stroke="#444" stroke-width="1.5"><path d="M1 3h4l3 12h12l3-9H6"/><circle cx="9" cy="19" r="1.6"/><circle cx="18" cy="19" r="1.6"/></svg><span>SHOP NOW</span><svg viewBox="0 0 24 24"><path d="M12 21 3 12a5 5 0 0 1 9-7 5 5 0 0 1 9 7z" fill="#111"/></svg></div>
</div>

<section class="abs goal">
  <h2>OUR GOAL</h2>
  <div class="goal-card" style="left:112px">
    <div class="img" role="img" aria-label="Green landscape with a tree peeling away to reveal dry cracked earth" style="background:linear-gradient(100deg,#8fb36b,#c7c9cc 50%,#c9a06b)"></div>
    <h3>GLOBAL WARMING</h3>
  </div>
  <div class="goal-card" style="left:627px">
    <div class="img" role="img" aria-label="Pharmacist handling medicine boxes on a shelf" style="background:linear-gradient(170deg,#d9d6d2,#8c8576 55%,#3d4a50)"></div>
    <h3>RAW MATERIAL SHORTAGES</h3>
  </div>
</section>

<div class="abs about-ring"></div>
<div class="abs about-img" role="img" aria-label="Box of assorted plastic syringes and vials"></div>
<h2 class="abs about-title"><span class="accent">ABOUT</span> <span class="rest">US</span></h2>
<p class="abs about-text" style="top:2123px">There are many variations of passages of Lorem Ipsum available, but the majority have suffered alteration in some form, by injected humour, or randomised words which don't look even slightly believable. If you are going to use a passage of Lorem Ipsum, you need to be sure there isn't anything embarrassing hidden in the middle of text. All the Lorem Ipsum generators on the Internet tend to repeat predefined chunks as necessary, making this the first true generator on the Internet. It uses a dictionary of over 200 Latin words, combined with a handful of model sentence structures, to generate Lorem Ipsum which looks reasonable. The generated Lorem Ipsum is therefore always free from repetition, injected humour, or non-characteristic words etc.</p>
<p class="abs about-text" style="top:2395px">There are many variations of passages of Lorem Ipsum available, but the majority have suffered alteration in some form, by injected humour, or randomised words which don't look even slightly believable.</p>
<a class="abs btn-read" href="#">READ MORE</a>

<footer class="abs footer">
  <svg class="curve" viewBox="0 0 1200 70" preserveAspectRatio="none"><path d="M0 0H1200V62Q600-62 0 62Z" fill="#fff"/></svg>
  <div class="footer-logo"><span class="dot"></span><span>QUIET<br>ORCHARD</span></div>
  <div class="fcol" style="left:420px"><h4>QUICK LINKS</h4><ul><li>HOME</li><li>ABOUT US</li><li>SERVICES</li><li>SHOP</li><li>OUR GOAL</li></ul></div>
  <div class="fcol" style="left:637px"><h4>QTHER LINKS</h4><ul><li>REFUND POLICY</li><li>DELIVERY INFORMATION</li><li>TERMS &amp; CONDITIONS</li><li>PRIVACY POLICY</li><li>CONTACT US</li></ul></div>
  <div class="fcol" style="left:892px"><h4>FIND US NOW</h4><p>48 Linden Row,<br>Maple Vale, Country<br>Name - 712 904</p><p style="margin-top:20px">+1 (555) 013 2290<br>M-F 9AM-5PM</p></div>
</footer>
<div class="cart-float"><svg viewBox="0 0 24 24" fill="none" stroke="#333" stroke-width="1.4"><path d="M1 3h4l3 12h12l3-9H6M9 9h11M9 12h10"/><circle cx="9" cy="19" r="1.6"/><circle cx="18" cy="19" r="1.6"/></svg></div>

<div class="abs bottombar">
  <div class="copy">Copyright © 2022 Quiet Orchard | All Rights Reserved</div>
  <div class="cards"><span></span><span></span><span></span><span></span></div>
</div>

</body>
</html>
```